Proposal Template Design

We are looking to have our proposal templates redesigned. attached are examples of what we have been using. as well as our current logo

```html
<!DOCTYPE html>
<html lang="en">
<head>
<meta charset="utf-8">
<title>Ridgeline Insulation Letterhead</title>
<link href="https://fonts.googleapis.com/css2?family=Poppins:wght@400;500;600;700&display=swap" rel="stylesheet">
<style>
:root{
  --navy:#0b2a6b;
  --deep:#07142e;
  --sky:#1a92d2;
  --ink:#222;
  --paper:#fff;
  --bg:#ececec;
}
html,body{margin:0;padding:0;width:1200px;height:3271px;overflow:hidden;background:var(--bg);font-family:'Poppins',sans-serif;}
.letterhead{position:absolute;left:50px;top:858px;width:1100px;height:1554px;background:var(--paper);box-shadow:0 6px 24px rgba(0,0,0,.18);overflow:hidden;}
.band{position:absolute;left:0;width:1100px;background:linear-gradient(90deg,var(--deep) 0%,var(--navy) 45%,var(--sky) 100%);}
.band-top{top:0;height:150px;}
.band-bottom{bottom:0;height:190px;}
.brand{position:absolute;left:65px;top:240px;display:flex;align-items:center;gap:14px;}
.brand-mark{width:46px;height:46px;background:var(--navy);}
.brand-name{font-weight:700;font-size:34px;color:var(--navy);line-height:1;}
.recipient{position:absolute;left:65px;top:500px;}
.recipient-name{font-weight:700;font-size:26px;color:var(--navy);margin:0;line-height:1.15;}
.recipient-address{font-weight:600;font-size:19px;color:var(--ink);margin:0;line-height:1.3;}
.body{position:absolute;left:65px;right:82px;top:626px;font-size:14.6px;line-height:17.6px;color:var(--ink);text-align:justify;}
.body p{margin:0 0 30px;}
.signoff{position:absolute;left:65px;top:1082px;font-size:16px;line-height:22px;font-weight:600;color:var(--ink);}
.signoff span{display:block;color:var(--navy);}
.contact{position:absolute;left:74px;top:1402px;list-style:none;margin:0;padding:0;color:#fff;font-size:18.5px;line-height:25.5px;}
.contact li{display:flex;align-items:center;gap:20px;}
.contact li:first-child{font-size:21px;}
.contact svg{width:16px;height:16px;flex:none;}
</style>
</head>
<body>
<div class="letterhead">
  <div class="band band-top" role="img" aria-label="Decorative header wave band in navy and sky blue"></div>

  <div class="brand">
    <div class="brand-mark"></div>
    <div class="brand-name">Ridgeline Insulation</div>
  </div>

  <div class="recipient">
    <h2 class="recipient-name">MARK DEVLIN</h2>
    <p class="recipient-address">STREET ADDRESS CITY,<br>STATE 00000</p>
  </div>

  <div class="body">
    <p>Notice Dear Mark : Lorem ipsum dolor sit amet, consectetur adipiscing elit. Aenean ut ipsum eget massa hendrerit vestibulum vel in velit. Donec pretium neque velit. Aliquam porta lectus nec mauris ornare venenatis. Vivamus non est turpis, et cursus sem. Mauris vehicula erat in diam auctor at bibendum nisl lacinia. Morbi imperdiet neque vehicula nunc convallis gravida. Vestibulum iaculis pretium placerat. Integer consequat, est sit amet facilisis eleifend, nibh nibh varius orci, eget dapibus arcu dui non purus. Pellentesque in magna mauris. Duis enim sapien, dictum vitae condimentum a, pulvinar vel lacus. Mauris et molestie nibh. Vestibulum vitae nulla at metus elementum porta sit amet interdum elit. Nulla sollicitudin neque eu nulla volutpat congue. Etiam pellentesque, velit id dapibus fermentum, turpis sapien ornare dui, ac tincidunt ligula odio congue purus. Nunc sed ante dui, in porta lectus. Cras nec sem lorem. In hac habitasse platea dictumst. Maecenas id diam quis dui porta tristique. Sed id egestas felis. Donec ullamcorper mattis posuere. Phasellus fermentum eleifend tortor dreams vel dapibus. Vestibulum ante ipsum. Sincerely, Daniel Reyes</p>
    <p>Notice Dear Mark : Lorem ipsum dolor sit amet, consectetur adipiscing elit. Aenean ut ipsum eget massa hendrerit vestibulum vel in velit. Donec pretium neque velit. Aliquam porta lectus nec mauris ornare venenatis. Vivamus non est turpis, et cursus sem. Mauris vehicula erat in diam auctor at bibendum nisl lacinia. Morbi imperdiet neque vehicula nunc convallis gravida. Vestibulum iaculis pretium placerat. Integer consequat, est si</p>
    <p>t amet facilisis eleifend, nibh nibh varius orci, eget dapibus arcu dui non purus. Pellentesque in magna mauris. Duis enim sapien, dictum vitae condimentum a, pulvinar vel lacus. Mauris et molestie nibh. Vestibulum vitae nulla at metus elementum porta sit amet interdum elit. Nulla sollicitudin neque eu nulla volutpat congue. Etiam pellentesque, velit id dapibus fermentum, turpis sapien ornare dui, ac tincidunt ligula odio congue purus. Nunc sed ante dui, in porta lectus. Cras nec sem lorem. In hac habitasse platea dictumst. Maecenas id diam quis dui porta tristique. Sed id egestas felis. Donec ullamcorper mattis posuere. Phasellus fermentum eleifend tortor dreams vel dapibus. Vestibulum ante ipsum. Sincerely, Daniel Reyes</p>
  </div>

  <div class="signoff">Sincerely,<span>Daniel Reyes</span></div>

  <div class="band band-bottom" role="img" aria-label="Decorative footer wave band in navy and sky blue"></div>

  <ul class="contact">
    <li><svg viewBox="0 0 16 16"><circle cx="8" cy="8" r="8" fill="#fff"/><path d="M5 4.5l1.6-.4 1 2-1 .8a6 6 0 002.5 2.5l.8-1 2 1-.4 1.6c-3.3.2-6.6-3.1-6.5-6.5z" fill="var(--sky)"/></svg>555-014-2278</li>
    <li><svg viewBox="0 0 16 16"><circle cx="8" cy="8" r="8" fill="#fff"/><rect x="4" y="5.5" width="8" height="5.5" fill="none" stroke="var(--sky)" stroke-width="1.2"/><path d="M4 5.5l4 3 4-3" fill="none" stroke="var(--sky)" stroke-width="1.2"/></svg>office@ridgelineinsulation.com</li>
    <li><svg viewBox="0 0 16 16"><circle cx="8" cy="8" r="8" fill="#fff"/><path d="M8 3.5a3 3 0 00-3 3c0 2.2 3 6 3 6s3-3.8 3-6a3 3 0 00-3-3z" fill="var(--sky)"/><circle cx="8" cy="6.5" r="1.1" fill="#fff"/></svg>P.O Box 210, Fairview Texas 75099</li>
    <li><svg viewBox="0 0 16 16"><circle cx="8" cy="8" r="8" fill="#fff"/><circle cx="8" cy="8" r="4" fill="none" stroke="var(--sky)" stroke-width="1.1"/><path d="M4 8h8M8 4c-2 2.5-2 5.5 0 8M8 4c2 2.5 2 5.5 0 8" fill="none" stroke="var(--sky)" stroke-width=".9"/></svg>ridgelineinsulation.com</li>
  </ul>
</div>
</body>
</html>
```